Vasko Lumen Entertainment

I need a web design for my Business for better online promotions and services.. The name of my company is Vasko Lumen its a entertainment company music, events, networking and so on.. What I do is help artist create and finish projects such as mix tapes, music videos, and book performances in order to create a platform and i also offer representation to help grow there brands or business... I also work with and help develop independent artists!!!

Target Market(s)

Hip hop and R&B industry

Industry/Entity Type

Entertainment Industry

Number of Pages Required

1 page

Requirements
Must have
• Must display My previous and upcoming work i want people to see the quality I provide in my service.. I have more videos that I want to upload on there to show more work.... I would like to bring all the separate promotions and campaigns that I previously had and currently have all one platform for everybody to see and to find more easily instead having everything so spread out..
Nice to have
• Creativity thats going to compliment my work and quality..

```html
<!DOCTYPE html>
<html lang="en">
<head>
<meta charset="utf-8">
<title>Vasko Lumen Entertainment — Latest Work</title>
<link rel="stylesheet" href="https://fonts.googleapis.com/css2?family=Ubuntu:wght@400;500;700&display=swap">
<style>
  :root {
    --red: #d0141e;
    --ink: #111111;
    --white: #ffffff;
    --grey-text: #9a9a9a;
    --stage-dark: #4a4a4c;
    --stage-mid: #8b8b8e;
    --stage-light: #b9b9bc;
  }
  * { box-sizing: border-box; margin: 0; padding: 0; }
  html, body { width: 1200px; height: 800px; overflow: hidden; background: var(--white); }
  body { font-family: "Ubuntu", sans-serif; position: relative; }

  .latest-work {
    position: absolute; left: 0; top: 0; width: 1200px; height: 520px;
    background: radial-gradient(ellipse at 60% 40%, var(--stage-light) 0%, var(--stage-mid) 45%, var(--stage-dark) 100%);
  }
  .section-title {
    position: absolute; left: 0; width: 100%; text-align: center;
    font-weight: 500; font-size: 28px; letter-spacing: 0.5px; text-transform: uppercase;
  }
  .latest-work .section-title { top: 22px; color: var(--white); }
  .accent { color: var(--red); }

  .work-grid {
    position: absolute; left: 183px; top: 90px; width: 834px;
    display: grid; grid-template-columns: 406px 406px; column-gap: 22px; row-gap: 26px;
  }
  .work-card {
    height: 80px; background: var(--white);
    border: 4px solid var(--ink); outline: 2px solid var(--white);
    display: flex; align-items: center; padding: 0 18px 0 14px;
  }
  .work-card .calendar { width: 34px; height: 34px; flex: none; }
  .work-card .date {
    margin-left: 24px; width: 56px; font-size: 12px; line-height: 15px; color: var(--grey-text);
  }
  .work-card .thumb { width: 36px; height: 36px; flex: none; margin-left: 14px; }
  .work-card .track {
    flex: 1; text-align: center; font-size: 11px; font-weight: 500; color: var(--ink);
  }
  .work-card .play { width: 20px; height: 20px; flex: none; }

  .view-more {
    position: absolute; left: 528px; top: 430px; width: 143px; height: 38px;
    background: var(--ink); color: var(--white); font-size: 12px; font-weight: 500;
    display: flex; align-items: center; justify-content: center; letter-spacing: 0.5px;
  }

  .gallery-band { position: absolute; left: 0; top: 520px; width: 1200px; height: 115px; background: var(--white); }
  .gallery-band .section-title { top: 38px; color: var(--ink); }

  .gallery-strip { position: absolute; left: 0; top: 635px; width: 1200px; height: 165px; display: flex; }
  .gallery-strip .photo { height: 100%; }
</style>
</head>
<body>
  <section class="latest-work" role="img" aria-label="Greyscale backdrop of a studio microphone over a mixing desk">
    <h2 class="section-title"><span class="accent">Latest</span> Work</h2>

    <div class="work-grid">
      <div class="work-card">
        <svg class="calendar" viewBox="0 0 34 34"><rect x="3" y="6" width="28" height="25" fill="none" stroke="#111" stroke-width="3"/><rect x="3" y="6" width="28" height="6" fill="#111"/><rect x="9" y="2" width="3" height="7" fill="#111"/><rect x="22" y="2" width="3" height="7" fill="#111"/><path d="M3 18h28M3 24h28M10 12v19M17 12v19M24 12v19" stroke="#111" stroke-width="2"/></svg>
        <div class="date">20 Jan<br>2017</div>
        <div class="thumb" role="img" aria-label="Artist portrait" style="background:linear-gradient(#9fb0b8,#5a7d86)"></div>
        <div class="track">Corvin Vale - Trance</div>
        <svg class="play" viewBox="0 0 20 20"><circle cx="10" cy="10" r="8" fill="none" stroke="#111" stroke-width="2"/><path d="M8 6l6 4-6 4z" fill="#111"/></svg>
      </div>
      <div class="work-card">
        <svg class="calendar" viewBox="0 0 34 34"><rect x="3" y="6" width="28" height="25" fill="none" stroke="#111" stroke-width="3"/><rect x="3" y="6" width="28" height="6" fill="#111"/><rect x="9" y="2" width="3" height="7" fill="#111"/><rect x="22" y="2" width="3" height="7" fill="#111"/><path d="M3 18h28M3 24h28M10 12v19M17 12v19M24 12v19" stroke="#111" stroke-width="2"/></svg>
        <div class="date">20 Jan<br>2017</div>
        <div class="thumb" role="img" aria-label="Artist portrait" style="background:linear-gradient(#9fb0b8,#5a7d86)"></div>
        <div class="track">Corvin Vale - Trance</div>
        <svg class="play" viewBox="0 0 20 20"><circle cx="10" cy="10" r="8" fill="none" stroke="#111" stroke-width="2"/><path d="M8 6l6 4-6 4z" fill="#111"/></svg>
      </div>
      <div class="work-card">
        <svg class="calendar" viewBox="0 0 34 34"><rect x="3" y="6" width="28" height="25" fill="none" stroke="#111" stroke-width="3"/><rect x="3" y="6" width="28" height="6" fill="#111"/><rect x="9" y="2" width="3" height="7" fill="#111"/><rect x="22" y="2" width="3" height="7" fill="#111"/><path d="M3 18h28M3 24h28M10 12v19M17 12v19M24 12v19" stroke="#111" stroke-width="2"/></svg>
        <div class="date">20 Jan<br>2017</div>
        <div class="thumb" role="img" aria-label="Hip hop group cover art" style="background:linear-gradient(#c9a227,#3a3a1a)"></div>
        <div class="track">Hip Hop Group - Get Low</div>
        <svg class="play" viewBox="0 0 20 20"><circle cx="10" cy="10" r="8" fill="none" stroke="#111" stroke-width="2"/><path d="M8 6l6 4-6 4z" fill="#111"/></svg>
      </div>
      <div class="work-card">
        <svg class="calendar" viewBox="0 0 34 34"><rect x="3" y="6" width="28" height="25" fill="none" stroke="#111" stroke-width="3"/><rect x="3" y="6" width="28" height="6" fill="#111"/><rect x="9" y="2" width="3" height="7" fill="#111"/><rect x="22" y="2" width="3" height="7" fill="#111"/><path d="M3 18h28M3 24h28M10 12v19M17 12v19M24 12v19" stroke="#111" stroke-width="2"/></svg>
        <div class="date">20 Jan<br>2017</div>
        <div class="thumb" role="img" aria-label="Artist portrait" style="background:linear-gradient(#9fb0b8,#5a7d86)"></div>
        <div class="track">Corvin Vale - Trance</div>
        <svg class="play" viewBox="0 0 20 20"><circle cx="10" cy="10" r="8" fill="none" stroke="#111" stroke-width="2"/><path d="M8 6l6 4-6 4z" fill="#111"/></svg>
      </div>
      <div class="work-card">
        <svg class="calendar" viewBox="0 0 34 34"><rect x="3" y="6" width="28" height="25" fill="none" stroke="#111" stroke-width="3"/><rect x="3" y="6" width="28" height="6" fill="#111"/><rect x="9" y="2" width="3" height="7" fill="#111"/><rect x="22" y="2" width="3" height="7" fill="#111"/><path d="M3 18h28M3 24h28M10 12v19M17 12v19M24 12v19" stroke="#111" stroke-width="2"/></svg>
        <div class="date">20 Jan<br>2017</div>
        <div class="thumb" role="img" aria-label="R&amp;B mix cover art" style="background:linear-gradient(#2f5fb3,#1a1a3a)"></div>
        <div class="track">R&amp;B Mix 2017 - Danger</div>
        <svg class="play" viewBox="0 0 20 20"><circle cx="10" cy="10" r="8" fill="none" stroke="#111" stroke-width="2"/><path d="M8 6l6 4-6 4z" fill="#111"/></svg>
      </div>
      <div class="work-card">
        <svg class="calendar" viewBox="0 0 34 34"><rect x="3" y="6" width="28" height="25" fill="none" stroke="#111" stroke-width="3"/><rect x="3" y="6" width="28" height="6" fill="#111"/><rect x="9" y="2" width="3" height="7" fill="#111"/><rect x="22" y="2" width="3" height="7" fill="#111"/><path d="M3 18h28M3 24h28M10 12v19M17 12v19M24 12v19" stroke="#111" stroke-width="2"/></svg>
        <div class="date">20 Jan<br>2017</div>
        <div class="thumb" role="img" aria-label="Artist portrait" style="background:linear-gradient(#9fb0b8,#5a7d86)"></div>
        <div class="track">Corvin Vale - Trance</div>
        <svg class="play" viewBox="0 0 20 20"><circle cx="10" cy="10" r="8" fill="none" stroke="#111" stroke-width="2"/><path d="M8 6l6 4-6 4z" fill="#111"/></svg>
      </div>
    </div>

    <div class="view-more">VIEW MORE</div>
  </section>

  <section class="gallery-band">
    <h2 class="section-title">Photo <span class="accent">Gallery</span></h2>
  </section>

  <div class="gallery-strip">
    <div class="photo" role="img" aria-label="Artist posing in a blue cap" style="width:183px;background:linear-gradient(135deg,#2c4a8a,#c9935a,#e0a33a)"></div>
    <div class="photo" role="img" aria-label="Artist portrait in a dark jacket" style="width:118px;background:linear-gradient(135deg,#c07a2a,#2a3a1e)"></div>
    <div class="photo" role="img" aria-label="Group of three artists in hats and jackets" style="width:300px;background:linear-gradient(90deg,#d8d2c8,#8a6a58,#3a2e2a)"></div>
    <div class="photo" role="img" aria-label="Two friends at a night event under blue lights" style="width:297px;background:linear-gradient(135deg,#1b2f7a,#0c1430,#3a2a10)"></div>
    <div class="photo" role="img" aria-label="Recording studio mixing console with red lights" style="width:302px;background:linear-gradient(160deg,#5a2a18,#141c3a,#0a0a14)"></div>
  </div>
</body>
</html>
```